Maple drift now Banner promoting freedom and adventure working from laptop

I need 3 different banners in 4 different sizes
I am an online business working from home on my laptop. I am in the motivational program and internet marketing industry and would like some banners that reflect healthy, fun and financially free lifestyle.
I have a Pallorum page title of KeyUpVibe and a website called Mapledriftnow.com
I have uploaded some photos but am unsure what may be required for the banners.
I am on the Gold Coast Australia but will be advertising in America, UK, Canada etc.

Target Market(s)

Adventure and Health fitness

Colors

Designer to choose colors to be used in the design.

Requirements
Must have
• Promotion of a living a financially free life through the ability of working from home via your own online business.
• Fun fit healthy freedom and adventure associated with someone living their dream life from working from home away from the 9 to 5 hustle and bussle.
Nice to have
• beaches, mountains and working from a Zen slate max.
• Showing fun and adventure from someone living this lifestyle.

```html
<!DOCTYPE html>
<html lang="en">
<head>
<meta charset="utf-8">
<title>Maple drift now – Create the lifestyle banner</title>
<link rel="stylesheet" href="https://fonts.googleapis.com/css2?family=Roboto:wght@400;500;700&display=swap">
<style>
  :root {
    --teal: #2ee6df;
    --white: #ffffff;
    --disc: rgba(12, 12, 12, 0.9);
    --ring: rgba(255, 255, 255, 0.85);
    --photo-light: #b9b6b0;
    --photo-mid: #6f6458;
    --photo-wood: #7a5a3e;
    --photo-dark: #1d1d22;
  }
  * { margin: 0; padding: 0; box-sizing: border-box; }
  html, body {
    width: 1200px;
    height: 1200px;
    overflow: hidden;
    background: var(--photo-dark);
  }
  .banner {
    position: relative;
    width: 1200px;
    height: 1200px;
    overflow: hidden;
    font-family: "Roboto", Arial, sans-serif;
  }
  .banner__photo {
    position: absolute;
    inset: 0;
    background:
      linear-gradient(160deg, rgba(0,0,0,0) 40%, rgba(10,10,14,0.75) 100%),
      radial-gradient(ellipse at 30% 25%, var(--photo-light) 0%, transparent 55%),
      linear-gradient(180deg, var(--photo-light) 0%, var(--photo-mid) 40%, var(--photo-wood) 65%, var(--photo-dark) 100%);
  }
  .headline-disc {
    position: absolute;
    left: 213px;
    top: 167px;
    width: 720px;
    height: 720px;
  }
  .headline-disc svg { position: absolute; inset: 0; }
  .headline {
    position: absolute;
    inset: 0;
    text-align: center;
  }
  .headline__line {
    position: absolute;
    left: 0;
    right: 0;
    line-height: 1;
  }
  .headline__line--soft {
    color: var(--teal);
    font-weight: 400;
    font-size: 92px;
    letter-spacing: -1px;
  }
  .headline__line--soft.l1 { top: 238px; }
  .headline__line--soft.l2 { top: 332px; }
  .headline__line--bold {
    color: var(--white);
    font-weight: 700;
    font-size: 76px;
    letter-spacing: 0;
  }
  .headline__line--bold.l3 { top: 445px; }
  .headline__line--bold.l4 { top: 522px; }
  .tagline {
    position: absolute;
    right: 52px;
    top: 1010px;
    text-align: right;
    color: var(--white);
    font-weight: 500;
    font-size: 38px;
    line-height: 50px;
  }
  .site-url {
    position: absolute;
    right: 52px;
    top: 1128px;
    color: var(--teal);
    font-weight: 400;
    font-size: 36px;
    letter-spacing: 3px;
  }
</style>
</head>
<body>
  <main class="banner">
    <div class="banner__photo" role="img" aria-label="Photo of a person in a checked shirt working at a wooden desk with a laptop, notebook and coffee cup"></div>

    <div class="headline-disc">
      <svg width="720" height="720" viewBox="0 0 720 720" aria-hidden="true">
        <circle cx="360" cy="360" r="360" fill="var(--disc)"/>
        <circle cx="360" cy="360" r="332" fill="none" stroke="var(--ring)" stroke-width="2.5"/>
      </svg>
      <h1 class="headline">
        <span class="headline__line headline__line--soft l1">Create</span>
        <span class="headline__line headline__line--soft l2">the lifestyle</span>
        <span class="headline__line headline__line--bold l3">YOU ALWAYS</span>
        <span class="headline__line headline__line--bold l4">WANTED</span>
      </h1>
    </div>

    <p class="tagline">WORK FROM HOME WITH<br>YOUR LAPTOP AND PHONE</p>
    <p class="site-url">www.mapledriftnow.com</p>
  </main>
</body>
</html>
```